Growing Your Label eBook Cover Design

I want to deisgn a cover for my eBook (FRONT COVER) and the title is:

Why I Grew a Six-Figure Label. So You Should Start
By KL Baxter

TITLE CHANGED TO: OUT OF DEBT INTO POWER; WHY I GREW A NINE-FIGURE FORTUNE SO YOU SHOULD START

The color palette is attached. Along with some photos options of me. Along with the ebook in WORD Document. My website is www.KLBaXterHub.com. You can use a different color palette if you think it is best

Target Market(s)

women who look to build a personal brand

Industry/Entity Type

health and wellness

Requirements
Must have
• the title
Nice to have
• use my picture on the cover; but that is optional
Should not have
• any men

```html
<!DOCTYPE html>
<html lang="en">
<head>
<meta charset="utf-8">
<title>Out of Debt Into Power — eBook Cover</title>
<link href="https://fonts.googleapis.com/css2?family=Bebas+Neue&family=Montserrat:wght@700;800&family=Josefin+Sans:wght@600&family=Great+Vibes&display=swap" rel="stylesheet">
<style>
  :root {
    --backdrop: #808080;
    --wine: #5b262b;
    --wine-deep: #3e0a0b;
    --peach: #f5cbbb;
    --peach-light: #fbe9e3;
    --blush-white: #fdf3f0;
    --ink: #3a1014;
    --white: #ffffff;
  }
  * { margin: 0; padding: 0; box-sizing: border-box; }
  html, body { width: 843px; height: 1200px; overflow: hidden; background: var(--backdrop); }
  .cover {
    position: absolute; left: 104px; top: 92px; width: 635px; height: 1017px;
    overflow: hidden;
    background: linear-gradient(90deg, var(--peach-light) 0%, var(--blush-white) 50%, var(--peach) 100%);
  }
  .cover__band {
    position: absolute; left: 76px; top: 0; width: 496px; height: 100%;
    background: linear-gradient(180deg, var(--wine) 0%, var(--wine) 45%, var(--wine-deep) 100%);
  }
  .kicker {
    position: absolute; left: 167px; top: 71px; width: 301px; height: 45px;
    background: var(--peach); transform: rotate(-3deg);
    box-shadow: 0 4px 8px rgba(0,0,0,.35);
    display: flex; align-items: center; justify-content: center;
    font: 800 24px 'Montserrat', sans-serif; color: var(--ink); letter-spacing: .5px;
  }
  .headline {
    position: absolute; left: 0; width: 100%; top: 112px; text-align: center;
    font: 262px/1 'Bebas Neue', sans-serif; color: var(--white);
    -webkit-text-stroke: 10px var(--ink); paint-order: stroke fill;
    letter-spacing: 2px;
  }
  .subline {
    position: absolute; left: 106px; width: 424px; top: 388px;
    display: flex; align-items: center; gap: 12px;
    font: 600 21px 'Josefin Sans', sans-serif; color: var(--peach-light); letter-spacing: 4px;
  }
  .subline::before, .subline::after { content: ""; flex: 1; height: 1.5px; background: var(--peach-light); }
  .fortune {
    position: absolute; left: 0; width: 100%; top: 422px; text-align: center;
    font: 64px/1 'Bebas Neue', sans-serif; color: var(--peach); letter-spacing: .5px;
  }
  .author-photo {
    position: absolute; left: 42px; top: 476px; width: 349px; height: 541px;
    border-radius: 140px 140px 0 0;
    background: linear-gradient(180deg, #2b1a1a 0%, #141010 40%, #1c1718 100%);
  }
  .promise {
    position: absolute; left: 424px; top: 522px;
    font: 800 40px/1.12 'Montserrat', sans-serif; color: var(--peach);
  }
  .promise__lead { display: block; font-size: 18px; color: var(--white); }
  .promise__you { color: var(--white); }
  .byline-script {
    position: absolute; left: 444px; top: 782px;
    font: 84px/1 'Great Vibes', cursive; color: var(--white);
  }
  .author-name {
    position: absolute; right: 101px; top: 893px;
    font: 700 33px 'Montserrat', sans-serif; color: var(--peach);
  }
</style>
</head>
<body>
  <main class="cover">
    <div class="cover__band"></div>
    <div class="kicker">OUT OF DEBT INTO</div>
    <h1 class="headline">POWER</h1>
    <p class="subline">WHY I GREW A</p>
    <p class="fortune">NINE-FIGURE FORTUNE</p>
    <div class="author-photo" role="img" aria-label="Photo of the author smiling, wearing a black turtleneck, raising one hand"></div>
    <p class="promise">
      <span class="promise__lead">So</span>
      <span class="promise__you">YOU</span><br>SHOULD<br>START
    </p>
    <p class="byline-script">By</p>
    <p class="author-name">KL BAXTER</p>
  </main>
</body>
</html>
```